Harbor Key Realty - New Agent Opportunity Overview

We want to create a one (1) page brochure to highlight what Harbor Key Realty (a real estate brokerage) offers new agents. I have uploaded a Word doc that has all the text we want on the flyer. We want a professional looking design.
Industry/Entity Type
Real Estate Agent
Colors
3176b5
33a6d7

```html
<!DOCTYPE html>
<html lang="en">
<head>
<meta charset="utf-8">
<title>Harbor Key Realty – New Agent Opportunity Overview</title>
<link rel="stylesheet" href="https://fonts.googleapis.com/css2?family=Bebas+Neue&family=Lato:wght@400;700&family=Montserrat:wght@500;700&family=Roboto:wght@500;700&display=swap">
<style>
  :root {
    --brand-blue: #3176b5;
    --bright-blue: #33a6d7;
    --hero-blue: #2f72b6;
    --navy: #0e2147;
    --ink: #101c3f;
    --text: #1b1e2b;
    --white: #ffffff;
    --page-bg: #e9eaec;
    --header-light: #f2f3f5;
  }
  * { box-sizing: border-box; margin: 0; padding: 0; }
  html, body { width: 1200px; height: 1117px; overflow: hidden; }
  body { background: var(--page-bg); position: relative; font-family: "Lato", sans-serif; color: var(--text); }

  .flyer {
    position: absolute; left: 180px; top: 15px;
    width: 910px; height: 1177px;
    transform: scale(0.9235); transform-origin: top left;
    background: var(--white);
    overflow: hidden;
  }

  .header {
    position: absolute; left: 0; top: 0; width: 910px; height: 165px;
    background: linear-gradient(160deg, #fafbfc 0%, #e8eaed 45%, #f7f8f9 60%, #e4e6e9 100%);
  }
  .brand-name {
    position: absolute; left: 40px; top: 54px;
    font-family: "Lato", sans-serif; font-weight: 700; font-size: 26px;
    letter-spacing: 4px; color: var(--ink);
  }
  .opening {
    position: absolute; right: 30px; top: 44px; text-align: right;
    font-family: "Montserrat", sans-serif; color: var(--ink);
  }
  .opening .location { font-weight: 500; font-size: 18px; letter-spacing: 0.3px; }
  .opening .status { font-weight: 700; font-size: 29px; margin-top: 2px; letter-spacing: 0.2px; }

  .hero { position: absolute; left: 0; top: 145px; width: 910px; height: 380px; }
  .hero svg { position: absolute; left: 0; top: 0; }
  .hero-title {
    position: absolute; left: 55px; top: 64px;
    font-family: "Bebas Neue", sans-serif; font-size: 72px; line-height: 71px;
    color: var(--white); letter-spacing: 0.5px; font-weight: 400;
  }
  .hero-cta {
    position: absolute; left: 0; top: 294px; width: 422px; height: 43px;
    background: var(--navy); border-radius: 0 6px 6px 0;
    font-family: "Bebas Neue", sans-serif; font-size: 38px; line-height: 45px;
    color: var(--white); padding-left: 57px; letter-spacing: 0.3px;
  }

  .section-title {
    font-family: "Roboto", sans-serif; font-weight: 700; font-size: 22px; color: var(--ink);
  }
  .bullets { list-style: none; font-size: 16px; line-height: 25px; }
  .bullets li::before { content: "•"; margin-right: 5px; }
  .bullets li.sub { padding-left: 25px; }
  .bullets li.sub::before { content: "o"; margin-right: 6px; }

  .advantage { position: absolute; left: 49px; top: 546px; width: 830px; }
  .advantage .cols, .support .cols { display: flex; margin-top: 10px; }
  .advantage .col:first-child, .support .col:first-child { width: 380px; padding-left: 2px; }

  .compensation {
    position: absolute; left: 0; top: 720px; width: 910px; height: 173px;
    background: var(--navy); color: var(--white);
  }
  .compensation .content { position: absolute; left: 49px; top: 20px; width: 370px; }
  .compensation .section-title { color: var(--white); }
  .compensation .bullets { margin-top: 6px; padding-left: 2px; }
  .compensation .bullets li { padding-left: 12px; text-indent: -12px; }

  .split-table {
    position: absolute; left: 417px; top: 708px; width: 467px;
    table-layout: fixed;
    border: 3px solid var(--brand-blue); border-radius: 7px;
    border-collapse: separate; border-spacing: 0; overflow: hidden;
    background: var(--white); font-size: 17px;
  }
  .split-table col.deal { width: 291px; }
  .split-table col.rate { width: 170px; }
  .split-table th {
    background: var(--brand-blue); color: var(--white);
    font-family: "Lato", sans-serif; font-weight: 700; font-size: 18px;
    text-align: left; height: 44px; padding: 0 0 0 24px; white-space: nowrap;
  }
  .split-table th.rate { padding-left: 12px; }
  .split-table td { height: 48px; padding-left: 24px; border-top: 3px solid var(--brand-blue); white-space: nowrap; }
  .split-table td.rate { padding-left: 12px; border-left: 3px solid var(--brand-blue); }

  .support { position: absolute; left: 48px; top: 922px; width: 830px; }
  .support .cols { margin-top: 14px; }
  .support .col:first-child { padding-left: 3px; }

  .footer {
    position: absolute; left: 0; top: 1118px; width: 910px; height: 59px;
    background: var(--brand-blue); color: var(--white);
    font-family: "Lato", sans-serif; font-size: 19px; letter-spacing: 7.5px;
    text-align: center; line-height: 59px;
  }
</style>
</head>
<body>
<main class="flyer">
  <header class="header">
    <div class="brand-name">HARBOR KEY REALTY</div>
    <div class="opening">
      <div class="location">HKR HOME CENTER GAITHERSBURG,</div>
      <div class="status">MARYLAND IS NOW OPEN</div>
    </div>
  </header>

  <section class="hero">
    <svg width="910" height="380" viewBox="0 0 910 380">
      <defs>
        <linearGradient id="heroBlue" x1="0" y1="0" x2="1" y2="1">
          <stop offset="0" stop-color="#2c6fb3"/>
          <stop offset="0.6" stop-color="#3479bd"/>
          <stop offset="1" stop-color="#2e73b7"/>
        </linearGradient>
        <radialGradient id="photoTone" cx="0.55" cy="0.5" r="0.7">
          <stop offset="0" stop-color="#36557f"/>
          <stop offset="0.6" stop-color="#1e3657"/>
          <stop offset="1" stop-color="#142845"/>
        </radialGradient>
      </defs>
      <rect x="560" y="0" width="350" height="22" fill="var(--header-light)"/>
      <path d="M0,0 H600 C628,0 646,8 660,20 V358 C640,372 618,380 590,380 H0 Z" fill="url(#heroBlue)"/>
      <path d="M910,20 H575 C462,20 418,100 418,188 C418,276 462,358 575,358 H910 Z" fill="#ffffff"/>
      <path role="img" aria-label="Photo of a businessman in a suit holding a glowing house outline above open hands"
            d="M910,35 H580 C480,35 435,110 435,188 C435,266 480,342 580,342 H910 Z" fill="url(#photoTone)"/>
    </svg>
    <h1 class="hero-title">IGNITE YOUR<br>REAL ESTATE<br>BUSINESS</h1>
    <div class="hero-cta">JOIN HARBOR KEY REALTY</div>
  </section>

  <section class="advantage">
    <h2 class="section-title">Consumer Direct Advantage</h2>
    <div class="cols">
      <ul class="bullets col">
        <li>Lender Referrals</li>
        <li>Listhaven Leads</li>
        <li>Shared Lender Leads</li>
        <li>Homefindr.net / NearbyNestListings.com</li>
      </ul>
      <ul class="bullets col">
        <li>Credit Trigger Campaigns</li>
        <li>Consumer Behavior Campaigns</li>
        <li>HKR Call Center Marketing Team</li>
        <li>HKR Sponsored Local Events</li>
      </ul>
    </div>
  </section>

  <section class="compensation">
    <div class="content">
      <h2 class="section-title">Maximized Compensation</h2>
      <ul class="bullets">
        <li>No desk fees. No royalty fees. No franchise fees.</li>
        <li>Company paid E&amp;O</li>
        <li>Transaction fee of $550 includes Transaction Coordinator</li>
      </ul>
    </div>
  </section>

  <table class="split-table">
    <colgroup><col class="deal"><col class="rate"></colgroup>
    <thead>
      <tr><th>Type of Deal</th><th class="rate">Commission Split</th></tr>
    </thead>
    <tbody>
      <tr><td>Self-Generated</td><td class="rate">90% / 10%</td></tr>
      <tr><td>Lender Referred Leads</td><td class="rate">70% / 30%</td></tr>
      <tr><td>HKR Generated Leads / Referrals</td><td class="rate">55% / 45%</td></tr>
    </tbody>
  </table>

  <section class="support">
    <h2 class="section-title">Complete Support System</h2>
    <div class="cols">
      <ul class="bullets col">
        <li>Powerful Suite of Cloud Based Tools</li>
        <li class="sub">IDX, CRM and Transaction Management</li>
        <li>HKR Call Center Support for Leads and Deals</li>
        <li>Transaction Coordinator</li>
        <li>Virtual Assistants Available</li>
      </ul>
      <ul class="bullets col">
        <li>24/7 Workspace Access</li>
        <li>Coaching / Mentoring</li>
        <li>Social Media / Marketing Expertise</li>
        <li>Nationwide Partnerships with Top Lenders</li>
      </ul>
    </div>
  </section>

  <footer class="footer">WWW.HARBORKEYREALTY.COM</footer>
</main>
</body>
</html>
```